Hair Care; Beauty Store

We need an E Commerce website with shopping cart functionality. An update of our other website www.velmarshopwares.com. A website we like the look, feel and functionality is: www.quorvashelf.com
The key functionality needed is:
• Shopping cart with Secure payment plugin:
1. Zentrix
• Blog with images and video postings
• Rotating Banner on homepage like www.quorvashelf.com
• Brindlow, Scovamel, Lumoraxe, driftcast updates (To and from option)
• Newsletter sign up (VIP Club)
• CRM – 8 step follow through (Ability to add this plug-in later)
• Discount codes
• Landing Page popup on first visit to sign up for VIP Club
• Newsletter
1. Create newsletter on website
2. Newsletter sent to subscribers
3. Opt out functionality
• Cpanel
• WYSIWYG editing
• WooCommerce or Virtue Mart cart
• Mobile compatible – Kelphone, Oslab and Mobile phones
• SEO
• Google Analytics
• Advertising windows. (time measured campaigns, Rotating)
• Search
• Required pages
1. Contact Us
2. Ordering Information
3. Return Policy
4. Guarantee
5. Testimonials – (With image)
-Reviews (Verified) – with product links like www.quorvashelf.com
6. Our Products
- Hair Care
- Beauty
- Mind and Soul

Target Market(s)

Shoppers

Industry/Entity Type

Hair And Beauty

Number of Pages Required

5+ page

Font styles to use
Sans Serif

Colors
9ccb3b
fbed22
0493ce
0555a3
e34197
a54499
6b449b
f37122

Requirements
Must have
• Shopping Cart
• Newsletter
• Advertising Banner
• Landing page pop up/Newsletter sign up
• Zentrix payment
• Search
• Blog
• WYSIWYG Cpanel
Nice to have
• CRM add on

```html
<!DOCTYPE html>
<html lang="en">
<head>
<meta charset="utf-8">
<title>Velmar Beauty – Hair care &amp; beauty store</title>
<link href="https://fonts.googleapis.com/css2?family=Roboto:ital,wght@0,400;0,500;0,700;1,400&family=Oswald:wght@400;500&display=swap" rel="stylesheet">
<style>
:root{
  --topbar:#efefef;
  --ink:#333333;
  --muted:#777777;
  --green:#3f9a3c;
  --orange:#f37122;
  --nav-top:#27a2e0;
  --nav-bottom:#0a7fc2;
  --nav-active:#2d2320;
  --blue:#0493ce;
  --purple:#6b449b;
  --yellow:#fbed22;
  --footer:#0b4fa0;
  --footer-dark:#111111;
  --dark-band:#1b1a17;
  --card-line:#dddddd;
}
*{margin:0;padding:0;box-sizing:border-box}
html,body{width:1200px;height:3169px;overflow:hidden;background:#fff}
body{position:relative;font-family:"Roboto",Arial,sans-serif;color:var(--ink)}
.abs{position:absolute}

/* top bar */
.topbar{left:0;top:0;width:1200px;height:42px;background:var(--topbar);font-size:12px;color:#555}
.topbar .welcome{left:89px;top:14px}
.topbar .links{right:86px;top:14px;letter-spacing:.2px}

/* header */
.header{left:0;top:42px;width:1200px;height:127px;background:#fff}
.phone-ico{left:87px;top:43px;width:42px;height:42px;border:2px solid var(--orange);border-radius:50%;display:flex;align-items:center;justify-content:center}
.phone-num{left:144px;top:51px;font-size:20px;color:#333}
.brand{left:0;width:1200px;top:34px;text-align:center;color:var(--green);font-weight:500;line-height:1}
.brand .l1{font-size:31px;letter-spacing:5px}
.brand .l2{font-size:26px;letter-spacing:6px;margin-top:2px}
.round-ico{top:43px;width:44px;height:44px;border:2px solid var(--orange);border-radius:50%;display:flex;align-items:center;justify-content:center}
.badge{left:1084px;top:28px;width:24px;height:24px;border:2px solid #333;border-radius:50%;background:#fff;font-size:13px;text-align:center;line-height:20px}

/* nav */
.nav{left:0;top:169px;width:1200px;height:66px;background:linear-gradient(var(--nav-top),var(--nav-bottom))}
.nav .active{left:87px;top:0;width:124px;height:66px;background:var(--nav-active)}
.nav a{position:absolute;top:23px;transform:translateX(-50%);color:#fff;font-size:16px;text-decoration:none;letter-spacing:.3px}

/* hero */
.hero{left:0;top:235px;width:1200px;height:502px;background:linear-gradient(90deg,#c9b79d 0%,#d8c8ae 35%,#b98a5c 62%,#8a4a26 75%,#e9d6c4 100%)}
.hero-title{left:87px;top:183px;font-family:"Oswald",Arial,sans-serif;font-size:58px;color:#fff;line-height:1}
.hero-sub{left:87px;top:245px;font-family:"Oswald",Arial,sans-serif;font-size:44px;color:var(--yellow);line-height:1}
.hero-arrow{top:322px;width:36px;height:36px;border-radius:50%;background:#555;display:flex;align-items:center;justify-content:center}

/* welcome */
.welcome-title{left:0;width:1200px;top:798px;text-align:center;font-size:28px;font-weight:500;color:#222}
.welcome-title span{color:var(--blue)}
.welcome-text{left:127px;width:946px;top:843px;text-align:center;font-size:12.5px;line-height:22px;color:#777}

/* category tiles */
.tile{width:596px;height:317px}
.tile .photo{position:absolute;left:0;top:0;width:100%;height:256px}
.tile .label{position:absolute;left:0;top:256px;width:100%;height:61px;background:var(--purple);color:#fff;font-size:27px;font-weight:500;text-align:center;line-height:61px;letter-spacing:.5px}

/* testimonial */
.quote-band{left:0;top:1993px;width:1200px;height:361px;background:radial-gradient(ellipse at 50% 40%,#3a3528,var(--dark-band) 70%)}
.quote-band h2{position:absolute;left:0;width:1200px;top:46px;text-align:center;color:#fff;font-size:28px;font-weight:500}
.avatar{left:554px;top:112px;width:92px;height:92px;border-radius:50%;border:3px solid #fff;background:linear-gradient(#c98f6e,#7a4a33)}
.q-arrow{top:140px}
.quote-text{left:170px;width:860px;top:216px;text-align:center;color:#fff;font-size:15px;line-height:24px}
.quote-mark{font-size:34px;font-weight:700;color:#fff;position:absolute;top:208px}
.quote-name{left:0;width:1200px;top:278px;text-align:center;color:#fff;font-style:italic;font-size:16px}

/* blog */
.blog-title{left:0;width:1200px;top:2410px;text-align:center;font-size:28px;font-weight:500;color:#222}
.blog-title span{color:var(--blue)}
.card{top:2483px;width:317px;height:342px;border:1px solid var(--card-line);background:#fff}
.card .photo{position:absolute;left:4px;top:4px;width:307px;height:188px}
.card .date{position:absolute;left:0;top:44px;width:50px}
.card .date .d{background:var(--orange);color:#fff;text-align:center;height:54px;padding-top:6px;font-size:20px;line-height:22px}
.card .date .d small{display:block;font-size:10px}
.card .date .y{background:#2d2a28;color:#fff;text-align:center;height:48px;line-height:48px;font-size:15px}
.card h3{position:absolute;left:0;width:100%;top:206px;text-align:center;font-size:16px;font-weight:400;color:#222}
.card p{position:absolute;left:22px;width:273px;top:236px;text-align:center;font-size:12px;line-height:19px;color:#777}
.card .more{position:absolute;left:0;width:100%;top:304px;text-align:center;font-size:14px;color:var(--purple)}

/* footer */
.footer{left:0;top:2867px;width:1200px;height:218px;background:var(--footer);color:#fff}
.footer h4{position:absolute;top:40px;font-size:15px;font-weight:700}
.footer .txt{position:absolute;font-size:12.5px;line-height:20px}
.footer .email{position:absolute;left:89px;top:122px;width:216px;height:30px;background:#fff;color:#999;font-size:12px;padding:8px 8px}
.footer .sub{position:absolute;left:89px;top:162px;width:96px;height:30px;background:#2d2d2d;font-size:11px;text-align:center;line-height:30px}
.social{position:absolute;left:963px;display:flex;align-items:center;font-size:13px}
.social i{display:block;width:30px;height:30px;border:2px solid #fff;border-radius:50%;margin-right:20px}
.bottom{left:0;top:3085px;width:1200px;height:84px;background:var(--footer-dark);color:#fff}
.pay{position:absolute;top:32px;display:flex;gap:10px;left:89px}
.pay span{display:block;width:42px;height:22px;background:#fff;color:#333;font-size:9px;font-weight:500;text-align:center;line-height:22px}
.copyright{position:absolute;right:92px;top:34px;font-size:12px}
</style>
</head>
<body>

<div class="abs topbar">
  <div class="abs welcome">WELCOME TO VELMARBEAUTY</div>
  <div class="abs links">MY ACCOUNT &nbsp;|&nbsp; COMPARE &nbsp;|&nbsp; WISHLIST &nbsp;|&nbsp; DELIVERY &nbsp;|&nbsp; HELP &nbsp;|&nbsp; CHECKOUT &nbsp; € &nbsp;£ &nbsp;$</div>
</div>

<header class="abs header">
  <div class="abs phone-ico">
    <svg width="20" height="20" viewBox="0 0 24 24"><path fill="#f37122" d="M6.6 10.8a15.1 15.1 0 0 0 6.6 6.6l2.2-2.2c.3-.3.7-.4 1-.2 1.1.4 2.3.6 3.6.6.6 0 1 .4 1 1V20c0 .6-.4 1-1 1A17 17 0 0 1 3 4c0-.6.4-1 1-1h3.5c.6 0 1 .4 1 1 0 1.3.2 2.5.6 3.6.1.3 0 .7-.2 1z"/></svg>
  </div>
  <div class="abs phone-num">800-555-0148</div>
  <div class="abs brand"><div class="l1">VELMAR</div><div class="l2">BEAUTY</div></div>
  <div class="abs round-ico" style="left:994px">
    <svg width="20" height="20" viewBox="0 0 24 24"><circle cx="10" cy="10" r="6.5" fill="none" stroke="#f37122" stroke-width="3"/><path d="M15 15l6 6" stroke="#f37122" stroke-width="3" stroke-linecap="round"/></svg>
  </div>
  <div class="abs round-ico" style="left:1049px">
    <svg width="20" height="20" viewBox="0 0 24 24"><path fill="#f37122" d="M2 3h3l2.6 11h11l2.4-8H7" /><path d="M2 3h3l2.6 11h11l2.4-8H6.5" fill="none" stroke="#f37122" stroke-width="2"/><circle cx="9" cy="19" r="2" fill="#f37122"/><circle cx="17" cy="19" r="2" fill="#f37122"/></svg>
  </div>
  <div class="abs badge">0</div>
</header>

<nav class="abs nav">
  <div class="abs active"></div>
  <a style="left:149px">HOME</a>
  <a style="left:281px">PRODUCTS</a>
  <a style="left:423px">SERVICES</a>
  <a style="left:562px">ABOUT US</a>
  <a style="left:704px">OREDER</a>
  <a style="left:820px">SHOP</a>
  <a style="left:925px">NEWS</a>
  <a style="left:1050px">CONTACT</a>
</nav>

<section class="abs hero" role="img" aria-label="Banner photo of a smiling woman with long wavy auburn hair">
  <div class="abs hero-title">VELMAR BEAUTY</div>
  <div class="abs hero-sub">Hair care &amp; beauty store</div>
  <div class="abs hero-arrow" style="left:87px"><svg width="14" height="14" viewBox="0 0 14 14"><path d="M9 2L4 7l5 5" fill="none" stroke="#fff" stroke-width="2.2"/></svg></div>
  <div class="abs hero-arrow" style="left:128px"><svg width="14" height="14" viewBox="0 0 14 14"><path d="M5 2l5 5-5 5" fill="none" stroke="#fff" stroke-width="2.2"/></svg></div>
</section>

<h1 class="abs welcome-title">WELCOME TO <span>VELMAR BEAUTY</span></h1>
<p class="abs welcome-text">Human hair comes in many colors and textures, and are all made with a protein called keratin. Keratin is the same tough, water insoluble structural material that human nails are made of. Hair also contains natural oils (lipids) and water. These hair components are arranged in 3 primary structures: the cuticle the inside of the hair consisting of bundles of protein filaments, it helps to support the hair &amp; strength and alsomakes up the biggest portion of the hair</p>

<div class="abs tile" style="left:0;top:980px"><div class="photo" role="img" aria-label="Woman among white and pink roses" style="background:linear-gradient(90deg,#efe6dc,#d9b59c 50%,#f1ebe3)"></div><div class="label">SKIN TYPE</div></div>
<div class="abs tile" style="left:604px;top:980px"><div class="photo" role="img" aria-label="Fresh green herbs with amber oil bottles" style="background:linear-gradient(90deg,#3f7a2e,#6aa845 55%,#b77a2c 80%,#e9e0c8)"></div><div class="label">BESTSELLERS</div></div>
<div class="abs tile" style="left:0;top:1304px"><div class="photo" role="img" aria-label="Oil bottle with white jasmine flowers on turquoise wood" style="background:linear-gradient(135deg,#8fd3d6,#cfeeea 45%,#f4f1e2)"></div><div class="label">BODY CARE</div></div>
<div class="abs tile" style="left:604px;top:1304px"><div class="photo" role="img" aria-label="Woman applying face cream before a mirror" style="background:linear-gradient(90deg,#e8efe4,#cfe0c0 50%,#f3ede6)"></div><div class="label">FACE CARE</div></div>
<div class="abs tile" style="left:0;top:1625px"><div class="photo" role="img" aria-label="Woman with long glossy brown hair in profile" style="background:linear-gradient(100deg,#5b3b27,#9a6a45 45%,#c9a07c 70%,#efe9e2)"></div><div class="label">LIVING HAIR</div></div>
<div class="abs tile" style="left:604px;top:1625px"><div class="photo" role="img" aria-label="Green cosmetic bottles with a pink gerbera flower" style="background:linear-gradient(90deg,#e6ecef,#2f6a55 30%,#e9edf0 50%,#e0557a 62%,#2f6a55 85%,#e6ecef)"></div><div class="label">NEW COLLECTION</div></div>

<section class="abs quote-band" role="img" aria-label="Dark background of a bowl of herbal hair powder">
  <h2>LATEST FROM THE BLOG</h2>
  <div class="abs q-arrow" style="left:508px"><svg width="20" height="28" viewBox="0 0 20 28"><path d="M15 3L5 14l10 11" fill="none" stroke="#fff" stroke-width="3.5"/></svg></div>
  <div class="abs avatar" role="img" aria-label="Reviewer portrait"></div>
  <div class="abs q-arrow" style="left:672px"><svg width="20" height="28" viewBox="0 0 20 28"><path d="M5 3l10 11-10 11" fill="none" stroke="#fff" stroke-width="3.5"/></svg></div>
  <span class="quote-mark" style="left:160px">“</span>
  <p class="abs quote-text">Lorem Ipsum has been the industry's standard dummy text ever since the 1500s, when an unknown printer took a galley of type and scrambled it to make a type specimen book. It has survived not only five centuries</p>
  <span class="quote-mark" style="left:870px;top:234px">”</span>
  <div class="abs quote-name">Neque porro quisquam</div>
</section>

<h2 class="abs blog-title">LATEST FROM <span>THE BLOG</span></h2>

<article class="abs card" style="left:95px">
  <div class="photo" role="img" aria-label="Halved coconut with a jug of oil" style="background:linear-gradient(90deg,#f4f1ec,#8a5a33 40%,#d9a536 70%,#eee7dc)"></div>
  <div class="date"><div class="d">02<small>JUN</small></div><div class="y">2016</div></div>
  <h3>ANTI-HAIR LOSS ROUTINE</h3>
  <p>Lorem ipsum dolor sit amet, consectetur adipiscing elit. Sed blandit massa vel mauris sollicitudin dignis-sim. Lorem ipsum dolor sit amet.</p>
  <div class="more">Read More »</div>
</article>
<article class="abs card" style="left:442px">
  <div class="photo" role="img" aria-label="Woman with voluminous blonde curls" style="background:linear-gradient(90deg,#f0e4d4,#d8a872 45%,#c08850 70%,#f2e6d6)"></div>
  <div class="date"><div class="d">02<small>JUN</small></div><div class="y">2016</div></div>
  <h3>Neque porro quisquam</h3>
  <p>Lorem ipsum dolor sit amet, consectetur adipiscing elit. Sed blandit massa vel mauris sollicitudin dignis-sim. Lorem ipsum dolor sit amet.</p>
  <div class="more">Read More »</div>
</article>
<article class="abs card" style="left:790px">
  <div class="photo" role="img" aria-label="Woman with long hair flowing under water" style="background:linear-gradient(160deg,#1d4fa0,#3f7fc8 45%,#e9d9a0 75%,#6c8ad0)"></div>
  <div class="date"><div class="d">02<small>JUN</small></div><div class="y">2016</div></div>
  <h3>LONGER HAIR FAST</h3>
  <p>Lorem ipsum dolor sit amet, consectetur adipiscing elit. Sed blandit massa vel mauris sollicitudin dignis-sim. Lorem ipsum dolor sit amet.</p>
  <div class="more">Read More »</div>
</article>

<footer class="abs footer">
  <h4 style="left:89px">NEWSLETTERS SIGN UP</h4>
  <div class="txt" style="left:89px;top:71px;width:230px;line-height:18px">Sign up for our daily email by entering your information below</div>
  <div class="email">Email address</div>
  <div class="sub">SUBSCRIBE</div>

  <h4 style="left:380px">NEQUE PORRO QUISQUAM</h4>
  <div class="txt" style="left:380px;top:70px;width:226px;line-height:19px;text-align:justify">Lorem Ipsum has been the industry's standard dummy text ever since the 1500s, when an unknown printer took a galley of type and scrambled it to make a type specimen book.</div>

  <h4 style="left:674px">GET IN TOUCH</h4>
  <div class="txt" style="left:676px;top:82px;font-size:12px;line-height:23px">ADDRESS : 2270 LARKFIELD AVENUE<br>SUITE 210 DUNMORE, CA 90117<br>PHONE : 800-555-0148<br>EMAIL : INFO@VELMARSHOPWARES.COM</div>

  <h4 style="left:963px">FOLLOW US ON</h4>
  <div class="social" style="top:86px"><i></i>Brindlow</div>
  <div class="social" style="top:131px"><i></i>Chirpwell</div>
  <div class="social" style="top:175px"><i></i>Lumoraxe</div>
</footer>

<div class="abs bottom">
  <div class="pay"><span>Zentrix</span><span>Corvane</span><span>Talvo</span><span>Nexory</span><span>Ambrel</span></div>
  <div class="copyright">Copyright © 2016 &nbsp;All Rights Reserved</div>
</div>

</body>
</html>
```